1300 Cratelofn Van wrap

We are forklift mechanics.
Design a simple wrap to suit our 4 vans with our logo.
Add some colour/design using the base colours happy to add other colours as suits and highlights/shadows to balance/break up the white but not over power it.
Include mobile number 0491 570 266

```html
<!DOCTYPE html>
<html lang="en">
<head>
<meta charset="utf-8">
<title>1300 Cratelofn Van Wrap</title>
<link href="https://fonts.googleapis.com/css2?family=Oswald:wght@500;700&family=Poppins:wght@600;700&display=swap" rel="stylesheet">
<style>
  :root{
    --backdrop:#ebebeb;
    --van-white:#eeede8;
    --brand-red:#d42a2a;
    --ink:#141414;
    --paper:#ffffff;
    --head:'Oswald', sans-serif;
    --body:'Poppins', sans-serif;
  }
  html,body{margin:0;padding:0;overflow:hidden;}
  body{width:1200px;height:1200px;background:var(--backdrop);position:relative;}
  .wrap-panel{position:absolute;left:195px;width:810px;height:280px;}
  .wrap-panel--standard{top:210px;}
  .wrap-panel--diagonal{top:700px;}
  .head{font-family:var(--head);}
  .body{font-family:var(--body);}
</style>
</head>
<body>

<svg class="wrap-panel wrap-panel--standard" viewBox="0 0 810 280" role="img" aria-label="Side wrap layout, white base with red lower band">
  <rect class="panel-base" x="0" y="0" width="810" height="280" rx="24" fill="var(--van-white)"/>
  <!-- brand block -->
  <text class="head brand-name" x="418" y="78" font-size="56" font-weight="700" fill="var(--brand-red)" textLength="332" lengthAdjust="spacingAndGlyphs">1300 CRATELOFN</text>
  <rect class="tagline-bar" x="418" y="88" width="332" height="28" fill="var(--ink)"/>
  <text class="head tagline" x="584" y="109" font-size="19" font-weight="500" fill="var(--paper)" text-anchor="middle" textLength="320" lengthAdjust="spacingAndGlyphs">HIRE - SALES - SERVICE - REPAIRS</text>
  <!-- company box -->
  <rect class="company-box" x="170" y="140" width="122" height="50" fill="var(--brand-red)"/>
  <text class="body company-name" font-size="9.5" font-weight="700" fill="var(--ink)">
    <tspan x="180" y="158">NORTHVALE</tspan>
    <tspan x="180" y="170">LIFT SERVICE</tspan>
    <tspan x="180" y="182">P/L</tspan>
  </text>
  <!-- contact -->
  <text class="body phone" x="398" y="162" font-size="25" font-weight="700" fill="var(--brand-red)">0491 570 266</text>
  <text class="body web" x="398" y="183" font-size="12.5" font-weight="600" fill="var(--ink)">www.1300cratelofn.com.au</text>
  <text class="body service-note" font-size="13" font-weight="700" fill="var(--brand-red)" text-anchor="middle">
    <tspan x="690" y="150">ALL MAKES ONSITE</tspan>
    <tspan x="690" y="166">SERVICE</tspan>
  </text>
  <!-- lower band -->
  <rect class="lower-rule" x="160" y="222" width="610" height="5" fill="var(--ink)"/>
  <rect class="lower-band" x="160" y="231" width="432" height="34" fill="var(--brand-red)"/>
</svg>

<svg class="wrap-panel wrap-panel--diagonal" viewBox="0 0 810 280" role="img" aria-label="Side wrap layout with diagonal red rear section">
  <defs>
    <clipPath id="panel-clip"><rect x="0" y="0" width="810" height="280" rx="24"/></clipPath>
  </defs>
  <g clip-path="url(#panel-clip)">
    <rect class="panel-base" x="0" y="0" width="810" height="280" fill="var(--van-white)"/>
    <polygon class="rear-red" points="600,0 810,0 810,280 440,280" fill="var(--brand-red)"/>
    <polygon class="diagonal-strip" points="572,0 600,0 440,280 412,280" fill="var(--ink)"/>
  </g>
  <text class="head brand-name" transform="translate(415 262) rotate(-60.3)" font-size="46" font-weight="700" fill="var(--brand-red)" textLength="290" lengthAdjust="spacingAndGlyphs">1300 CRATELOFN</text>
  <text class="head tagline" transform="translate(440 264) rotate(-60.3)" font-size="14" font-weight="500" fill="var(--paper)" letter-spacing="2" textLength="290" lengthAdjust="spacingAndGlyphs">HIRE - SALES - SERVICE - REPAIRS</text>
  <!-- contact -->
  <text class="body phone" x="122" y="150" font-size="25" font-weight="700" fill="var(--brand-red)">0491 570 266</text>
  <text class="body web" x="142" y="170" font-size="13" font-weight="600" fill="var(--ink)">1300cratelofn.com.au</text>
  <!-- company name on red -->
  <rect class="company-mark" x="632" y="36" width="34" height="34" fill="var(--ink)"/>
  <text class="body company-name" font-size="12" font-weight="700" fill="var(--ink)">
    <tspan x="676" y="44">NORTHVALE</tspan>
    <tspan x="676" y="60">LIFT</tspan>
    <tspan x="676" y="76">SERVICE P/L</tspan>
  </text>
  <text class="body service-note" font-size="13" font-weight="700" fill="var(--paper)" text-anchor="middle">
    <tspan x="698" y="150">ALL MAKES ONSITE</tspan>
    <tspan x="698" y="166">SERVICE</tspan>
  </text>
</svg>

</body>
</html>
```